Power Generation Company needs a stationary design

We need a design for our letter envelope, A4 Envelope and letterhead. Our company name is BRIMVolt which i attached here sample our our call card. We are based in the Ardena and is into the Power Generation business. We own power facilities like Hydropower plant, Solar Power Plant, Diesel Power Plant, Gas Turbine Power Plant. We sell our power to various electric distribution companies, factories and office buildings.

Target Market(s)

Electric Distribution Companies and Factories

Industry/Entity Type

It Company

Colors
ec1f27

Requirements
Must have
• Logo and company name
Nice to have
• No specific
Should not have
• No specific

```html
<!DOCTYPE html>
<html lang="en">
<head>
<meta charset="utf-8">
<title>BRIMVolt Stationery</title>
<link rel="stylesheet" href="https://fonts.googleapis.com/css2?family=Open+Sans:wght@400;600&display=swap">
<style>
  :root {
    --brand-red: #ec1f27;
    --ink: #222222;
    --paper: #ffffff;
    --backdrop: #e9e4df;
    --edge: #d6d1cc;
  }
  * { box-sizing: border-box; margin: 0; padding: 0; }
  html, body {
    width: 1200px; height: 814px; overflow: hidden;
    background: var(--backdrop);
    font-family: "Open Sans", Arial, sans-serif;
    color: var(--ink);
  }
  .stationery { position: relative; width: 1200px; height: 814px; }

  .sheet {
    position: absolute;
    background: var(--paper);
    border: 1px solid var(--edge);
  }

  .brand { display: flex; align-items: center; gap: 8px; }
  .brand-dot {
    width: 22px; height: 22px; border-radius: 50%;
    border: 3px solid var(--brand-red);
  }
  .brand-name {
    color: var(--brand-red);
    font-weight: 600;
    font-size: 24px;
    letter-spacing: 3px;
    line-height: 1;
  }
  .brand-sub {
    color: var(--brand-red);
    font-weight: 400;
    font-size: 8px;
    letter-spacing: 4px;
    margin-top: 4px;
    margin-left: 30px;
  }

  /* Letterhead */
  .letterhead { left: 60px; top: 57px; width: 495px; height: 700px; }
  .letterhead .brand-block { position: absolute; left: 36px; top: 34px; }
  .letterhead .rule {
    position: absolute; left: 36px; right: 36px; bottom: 92px;
    height: 2px; background: var(--brand-red);
  }
  .letterhead .contact {
    position: absolute; left: 36px; right: 36px; bottom: 34px;
    text-align: center; font-size: 9px; line-height: 1.55;
  }
  .contact .label { color: var(--brand-red); }

  /* Envelope */
  .envelope { left: 600px; top: 237px; width: 540px; height: 340px; }
  .envelope .brand-block { position: absolute; left: 30px; top: 28px; }
  .envelope .rule {
    position: absolute; left: 30px; right: 30px; bottom: 70px;
    height: 2px; background: var(--brand-red);
  }
  .envelope .address {
    position: absolute; left: 30px; right: 30px; bottom: 46px;
    font-size: 9px;
  }
</style>
</head>
<body>
<main class="stationery">

  <section class="sheet letterhead" aria-label="Letterhead">
    <div class="brand-block">
      <div class="brand">
        <span class="brand-dot"></span>
        <span class="brand-name">BRIMVOLT</span>
      </div>
      <div class="brand-sub">BRIMVOLT INC</div>
    </div>
    <div class="rule"></div>
    <p class="contact">
      <span class="label">P:</span> +99-555-0140
      <span class="label">F:</span> +99-555-0141
      <span class="label">E:</span> info@brimvolt-net.com<br>
      48 Solana Business Tower, 902 Narra Ave., Lumen Business Park<br>
      Northgate, Velmora City, 4410, Ardena
    </p>
  </section>

  <section class="sheet envelope" aria-label="Envelope">
    <div class="brand-block">
      <div class="brand">
        <span class="brand-dot"></span>
        <span class="brand-name">BRIMVOLT</span>
      </div>
      <div class="brand-sub">BRIMVOLT INC</div>
    </div>
    <div class="rule"></div>
    <p class="address">48 Solana Business Tower, 902 Narra Ave., Lumen Business Park, Northgate, Velmora City, 4410, Ardena</p>
  </section>

</main>
</body>
</html>
```